Real estate investor business card to retire young ;)!

I need a logo design and a business card. I am based in Montreal, Canada. I buy multi-family properties and do lots development. The final design should communicate that I am a problem solver and reliable.

This card will be given to other investors, to potential sellers and industry experts.

Target Market(s)

Real estate community, multi-family owners

Industry/Entity Type

Real Estate Development

Contact Information for Business Card

My name: Lorna Vickery
email: immo.lorna.vickery@quellmail.example
cellphone: (555) 274-3916

Logo Text

Gestion immobilière

Font styles to use
Sans Serif

Colors
3176b5

Requirements
Must have
• Within 1-2 seconds the person who sees my card should know that I buy properties and lot. Areas to for Phone number and email adress. I do not have a business name. The card should simply state my name and what I do. The logo should be remembered by the person who reads my card
Should not have
• Colors too bright. Too much small details. I want something balanced, bold without being agressive.

```html
<!DOCTYPE html>
<html lang="fr">
<head>
<meta charset="utf-8">
<title>Lorna Vickery – Carte d'affaires</title>
<link rel="stylesheet" href="https://fonts.googleapis.com/css2?family=Barlow:wght@500;700&display=swap">
<style>
  :root {
    --brand-blue: #3180f2;
    --icon-light: #5fd0f5;
    --icon-deep: #2a6fe6;
    --page-bg: #ffffff;
    --card-light: #fbfcfc;
    --card-mid: #eef1f1;
    --card-shade: #dfe4e4;
  }
  * { margin: 0; padding: 0; box-sizing: border-box; }
  html, body {
    width: 1200px; height: 1200px; overflow: hidden;
    background: var(--page-bg);
    font-family: "Barlow", sans-serif;
  }
  .canvas { position: relative; width: 1200px; height: 1200px; }
  .card {
    position: absolute; left: 67px; top: 295px;
    width: 1066px; height: 609px; overflow: hidden;
  }
  .card-texture {
    position: absolute; inset: 0;
    background:
      radial-gradient(ellipse at 50% 40%, var(--card-light) 0%, rgba(251,252,252,0) 60%),
      radial-gradient(ellipse at 55% 100%, var(--card-shade) 0%, rgba(223,228,228,0) 55%),
      radial-gradient(ellipse at 70% 0%, var(--card-shade) 0%, rgba(223,228,228,0) 45%),
      linear-gradient(90deg, var(--card-light), var(--card-mid) 50%, var(--card-light));
  }
  .side-rail { position: absolute; top: 0; width: 30px; height: 609px; }
  .side-rail--left { left: 36px; }
  .side-rail--right { right: 36px; transform: scaleX(-1); }
  .content {
    position: absolute; inset: 0;
    display: flex; flex-direction: column; align-items: center;
  }
  .wordmark {
    margin-top: 118px;
    display: flex; align-items: center; gap: 12px;
    color: var(--brand-blue); font-weight: 700; font-size: 34px;
  }
  .wordmark-dot {
    width: 22px; height: 22px; border-radius: 50%;
    background: var(--brand-blue);
  }
  .holder-name {
    margin-top: 120px;
    color: var(--brand-blue); font-weight: 700; font-size: 76px;
    letter-spacing: 1px; line-height: 1;
  }
  .contact-list {
    margin-top: 96px; list-style: none;
    display: flex; flex-direction: column; align-items: center; gap: 12px;
  }
  .contact-item {
    display: flex; align-items: center; gap: 16px;
    color: var(--brand-blue); font-weight: 500; font-size: 36px;
    letter-spacing: 0.5px; line-height: 1;
  }
  .contact-icon { width: 35px; height: 38px; flex: none; }
</style>
</head>
<body>
<div class="canvas">
  <section class="card">
    <div class="card-texture" role="img" aria-label="Soft grey geometric network texture"></div>

    <svg class="side-rail side-rail--left" viewBox="0 0 30 609" aria-hidden="true">
      <rect x="2" y="0" width="3" height="609" fill="var(--brand-blue)"/>
      <path d="M2 140 L8 149 Q25 170 27 192 L27 420 Q25 442 8 463 L2 472 Z" fill="var(--brand-blue)"/>
    </svg>
    <svg class="side-rail side-rail--right" viewBox="0 0 30 609" aria-hidden="true">
      <rect x="2" y="0" width="3" height="609" fill="var(--brand-blue)"/>
      <path d="M2 140 L8 149 Q25 170 27 192 L27 420 Q25 442 8 463 L2 472 Z" fill="var(--brand-blue)"/>
    </svg>

    <div class="content">
      <div class="wordmark"><span class="wordmark-dot"></span>Gestion immobilière</div>
      <h1 class="holder-name">Lorna Vickery</h1>
      <ul class="contact-list">
        <li class="contact-item">
          <svg class="contact-icon" viewBox="0 0 35 38" aria-hidden="true">
            <circle cx="17.5" cy="20" r="17" fill="var(--icon-deep)"/>
            <circle cx="17.5" cy="17" r="17" fill="var(--icon-light)"/>
            <circle cx="17.5" cy="17" r="13" fill="#ffffff"/>
            <rect x="9.5" y="11" width="16" height="11" rx="1.5" fill="var(--icon-deep)"/>
            <path d="M10 12 L17.5 18 L25 12" fill="none" stroke="#ffffff" stroke-width="1.4"/>
          </svg>
          immo.lorna.vickery@quellmail.example
        </li>
        <li class="contact-item">
          <svg class="contact-icon" viewBox="0 0 35 38" aria-hidden="true">
            <circle cx="17.5" cy="20" r="17" fill="var(--icon-deep)"/>
            <circle cx="17.5" cy="17" r="17" fill="var(--icon-light)"/>
            <circle cx="17.5" cy="17" r="13" fill="#ffffff"/>
            <path d="M9 15 Q17.5 8 26 15 L24 17 L21 15 L14 15 L11 17 Z" fill="var(--icon-deep)"/>
            <rect x="12" y="16" width="11" height="7" rx="1.5" fill="var(--icon-deep)"/>
            <circle cx="17.5" cy="19.5" r="2" fill="#ffffff"/>
          </svg>
          (555) 274-3916
        </li>
      </ul>
    </div>
  </section>
</div>
</body>
</html>
```